Gin Bottle label

Hi, I would like a design based on a traditional, Vintage, Victorian type label.
The product is 'Hawthorn & Sloeberry Gin'
It will be 50cl and 40% vol.
The Gin will be dark brown in colour and attached is the types of bottle and a few ideas of the styles I like.
Many Thanks

```html
<!DOCTYPE html>
<html lang="en">
<head>
<meta charset="utf-8">
<title>Hawthorn &amp; Sloeberry Gin — Label</title>
<link rel="stylesheet" href="https://fonts.googleapis.com/css2?family=Rye&family=Pinyon+Script&family=IM+Fell+English+SC&family=Pathway+Gothic+One&display=swap">
<style>
  :root {
    --backdrop: #f5f5f7;
    --paper: #e7dfc6;
    --paper-edge: #d8cdae;
    --ink: #1b1712;
    --ornament: #c9bb97;
    --ornament-deep: #b6a67e;
  }
  * { margin: 0; padding: 0; box-sizing: border-box; }
  html, body {
    width: 1162px; height: 1200px; overflow: hidden;
    background: var(--backdrop);
  }
  .canvas {
    position: relative; width: 1162px; height: 1200px;
  }
  .label {
    position: absolute; left: 211px; top: 15px;
    width: 740px; height: 1170px;
    background: radial-gradient(ellipse at 50% 45%, var(--paper) 55%, var(--paper-edge) 100%);
    color: var(--ink);
  }
  .label-frame {
    position: absolute; inset: 0; width: 740px; height: 1170px;
  }
  .ornament {
    position: absolute;
    background: linear-gradient(135deg, var(--ornament), var(--ornament-deep));
    opacity: .55; border-radius: 10px;
  }
  .corner-tl { left: 28px; top: 28px; width: 96px; height: 150px; }
  .corner-tr { right: 28px; top: 28px; width: 96px; height: 150px; }
  .corner-bl { left: 28px; bottom: 48px; width: 96px; height: 150px; }
  .corner-br { right: 28px; bottom: 48px; width: 96px; height: 150px; }
  .swirl-left { left: 40px; top: 640px; width: 80px; height: 270px; border-radius: 40px; }
  .swirl-right { right: 40px; top: 640px; width: 80px; height: 270px; border-radius: 40px; }
  .flourish-bottom { left: 180px; top: 930px; width: 380px; height: 110px; border-radius: 55px; }

  .quality-banner {
    position: absolute; left: 230px; top: 70px; width: 280px; height: 56px;
    border: 3px solid var(--ink); border-radius: 6px;
    display: flex; align-items: center; justify-content: center;
    font-family: "IM Fell English SC", serif; font-size: 27px; letter-spacing: 2px;
  }
  .product-name {
    position: absolute; left: 0; right: 0; top: 175px;
    text-align: center; font-family: "Rye", serif; line-height: 1;
  }
  .product-name .line-one { display: block; font-size: 92px; }
  .product-name .ampersand { display: block; font-family: "Pinyon Script", cursive; font-size: 96px; margin: 18px 0 6px; }
  .product-name .line-two { display: block; font-size: 86px; }
  .product-type {
    position: absolute; left: 0; right: 0; top: 690px;
    text-align: center; font-family: "Pinyon Script", cursive; font-size: 190px; line-height: 1;
  }
  .details {
    position: absolute; left: 150px; right: 150px; top: 1050px;
    display: flex; justify-content: space-between;
    font-family: "Pathway Gothic One", sans-serif; font-size: 58px; line-height: 1;
  }
</style>
</head>
<body>
<main class="canvas">
  <section class="label">
    <svg class="label-frame" viewBox="0 0 740 1170" aria-hidden="true">
      <rect x="10" y="10" width="720" height="1150" fill="none" stroke="#1b1712" stroke-width="3"/>
      <rect x="20" y="20" width="700" height="1130" fill="none" stroke="#1b1712" stroke-width="1.5"/>
      <line x1="150" y1="1125" x2="590" y2="1125" stroke="#1b1712" stroke-width="6" stroke-linecap="round" stroke-dasharray="0 14"/>
    </svg>

    <div class="ornament corner-tl" role="img" aria-label="Victorian corner flourish"></div>
    <div class="ornament corner-tr" role="img" aria-label="Victorian corner flourish"></div>
    <div class="ornament corner-bl" role="img" aria-label="Victorian corner flourish"></div>
    <div class="ornament corner-br" role="img" aria-label="Victorian corner flourish"></div>
    <div class="ornament swirl-left" role="img" aria-label="Scrolled swirl ornament"></div>
    <div class="ornament swirl-right" role="img" aria-label="Scrolled swirl ornament"></div>
    <div class="ornament flourish-bottom" role="img" aria-label="Ornamental divider flourish"></div>

    <div class="quality-banner">Highest Quality</div>

    <h1 class="product-name">
      <span class="line-one">Hawthorn</span>
      <span class="ampersand">&amp;</span>
      <span class="line-two">Sloeberry</span>
    </h1>
    <p class="product-type">Gin</p>

    <div class="details">
      <span class="volume">50 cl</span>
      <span class="strength">40% vol.</span>
    </div>
  </section>
</main>
</body>
</html>
```